10 Page Marketing Report Template - Quillmont Care Associates

https://www.vexaclip.com/view/8f1d2e7b90c44a6f81e2d3b5c7a9f014

We are creating a professional, modern, and slightly edgy PDF-style report document (about 10 pages) to showcase the results of a client’s first 30 days with Quillmont Care Associates.

The report will be designed as a customizable Canva template so the Client Success team can easily update logos, screenshots, and text for each client.

This document will serve as both a visual presentation piece and a report deliverable, blending clean design, modern layout, and data-driven storytelling.

I am attaching the content for the report doc and the design brief along with the logo.
Here is our website for design style, look, and feel: https://quillmontcare.example/

Here is a quick overview video I made:

```html
<!DOCTYPE html>
<html lang="en">
<head>
<meta charset="utf-8">
<title>30 Days to Value Report – Quillmont Care Associates</title>
<link rel="stylesheet" href="https://fonts.googleapis.com/css2?family=Inter:wght@700;800&family=Outfit:wght@400;500&family=Lexend:wght@500&display=swap">
<style>
  :root {
    --navy: #33425f;
    --orange: #f7a21b;
    --orange-light: #ffc21a;
    --orange-deep: #f08a12;
    --white: #ffffff;
    --stage-top: #c9c9c9;
    --stage-bottom: #ffffff;
    --sky-top: #13294a;
    --sky-mid: #2a5585;
    --sky-low: #3d78b4;
  }
  * { box-sizing: border-box; margin: 0; padding: 0; }
  html, body { width: 1200px; height: 2344px; overflow: hidden; }
  body {
    position: relative;
    background: linear-gradient(180deg, var(--stage-top) 0%, var(--stage-bottom) 100%);
    font-family: "Outfit", sans-serif;
  }
  .page {
    position: absolute;
    left: 232px;
    width: 734px;
    height: 1038px;
    overflow: hidden;
    box-shadow: 8px 10px 14px rgba(0,0,0,0.45);
  }
  .page--cover { top: 81px; background: var(--white); }
  .page--intro { top: 1200px; }

  .wordmark {
    display: flex;
    flex-direction: column;
    align-items: center;
    color: var(--navy);
  }
  .wordmark__row { display: flex; align-items: center; gap: 18px; }
  .wordmark__square { width: 24px; height: 24px; background: var(--navy); }
  .wordmark__name {
    font-family: "Lexend", sans-serif;
    font-weight: 500;
    text-transform: uppercase;
    letter-spacing: 0.06em;
    line-height: 1.08;
    color: var(--navy);
  }
  .wordmark__tagline {
    font-family: "Lexend", sans-serif;
    font-weight: 500;
    text-transform: uppercase;
    letter-spacing: 0.16em;
    color: var(--navy);
  }

  .cover__brand {
    position: absolute;
    top: 130px; left: 0; width: 100%;
  }
  .cover__brand .wordmark__name { font-size: 35px; }
  .cover__brand .wordmark__tagline { font-size: 18px; margin-top: 18px; }

  .cover__band {
    position: absolute;
    top: 405px; left: 0;
    width: 734px; height: 633px;
    background: var(--navy);
  }
  .cover__art {
    position: absolute;
    top: 0; left: 0;
    width: 734px; height: 1038px;
  }
  .cover__title {
    position: absolute;
    top: 690px; left: 0; width: 100%;
    text-align: center;
    font-family: "Inter", sans-serif;
    font-weight: 800;
    font-size: 74px;
    line-height: 96px;
    letter-spacing: -0.01em;
    color: var(--navy);
  }
  .cover__subtitle {
    position: absolute;
    top: 898px; left: 0; width: 100%;
    text-align: center;
    font-size: 35px;
    font-weight: 400;
    color: var(--navy);
  }

  .intro__art {
    position: absolute; inset: 0;
    background:
      radial-gradient(ellipse 60% 45% at 72% 70%, rgba(120,180,240,0.55), transparent 70%),
      linear-gradient(180deg, var(--sky-top) 0%, var(--sky-mid) 50%, var(--sky-low) 100%);
  }
  .intro__brand {
    position: absolute;
    top: 31px; left: 393px;
    width: 341px; height: 113px;
    background: var(--white);
    justify-content: center;
  }
  .intro__brand .wordmark__name { font-size: 19px; }
  .intro__brand .wordmark__square { width: 14px; height: 14px; }
  .intro__brand .wordmark__row { gap: 12px; }
  .intro__brand .wordmark__tagline { font-size: 10px; margin-top: 8px; }
  .intro__copy {
    position: absolute;
    top: 236px; left: 50px;
    width: 385px;
    color: var(--white);
    font-size: 21px;
    line-height: 26.5px;
  }
  .intro__copy p + p { margin-top: 26px; }
</style>
</head>
<body>

  <section class="page page--cover">
    <div class="wordmark cover__brand">
      <div class="wordmark__row">
        <span class="wordmark__square"></span>
        <span class="wordmark__name">Quillmont<br>Care<br>Associates</span>
      </div>
      <span class="wordmark__tagline">Steady steps. Lasting care.</span>
    </div>

    <div class="cover__band"></div>
    <svg class="cover__art" viewBox="0 0 734 1038" role="img" aria-label="Golden rising bar chart with an upward arrow on a glowing orange surface">
      <defs>
        <linearGradient id="coverGlow" x1="0" y1="0" x2="0" y2="1">
          <stop offset="0" stop-color="#ffc21a"/>
          <stop offset="0.55" stop-color="#f7a21b"/>
          <stop offset="1" stop-color="#f08a12"/>
        </linearGradient>
      </defs>
      <polygon points="177,416 556,416 734,594 734,1038 0,1038 0,594" fill="url(#coverGlow)"/>
    </svg>

    <h1 class="cover__title">30 DAYS TO<br>VALUE REPORT</h1>
    <p class="cover__subtitle">Your First Month of Progress</p>
  </section>

  <section class="page page--intro">
    <div class="intro__art" role="img" aria-label="Glowing path winding up to the summit of a blue mountain under a night sky"></div>

    <div class="wordmark intro__brand">
      <div class="wordmark__row">
        <span class="wordmark__square"></span>
        <span class="wordmark__name">Quillmont<br>Care<br>Associates</span>
      </div>
      <span class="wordmark__tagline">Steady steps. Lasting care.</span>
    </div>

    <div class="intro__copy">
      <p>The first 30 days are about creating momentum. Our goal was to build the foundation for measurable growth — from your website and Lumora Places Profile to your SEO systems, audits, and backlink strategy.</p>
      <p>This report highlights what’s been accomplished and what’s next in your marketing journey.</p>
    </div>
  </section>

</body>
</html>
```